Silver Orchard Brochure

I would like to design an e-brochure to be sent to a particular fashion designer that we choose to invite to be featured on our platform. The brochure should reflect the existing brand image of the website. The brochure will probably have no more than four to five pages and will include the following information

1) Cover Page

2) About Us

3) Our Unique Edge

4) Member Benefits

5) Prices

6) Contact

hello designers think some people are confused about what the brochure is about i have uploaded a file with the sample text - hope this helps

Reason: Hi everyone I have extended the deadline as i have uploaded a text document for the brochure that should assist with thinking about the design. please email if you have questions

Hi I have got feedback that the document wasn't uploaded properly - the sample text to work with is now uploaded on docx format Thanks

Target Market(s)

Fashion designers

Industry/Entity Type

Fashion

Requirements
Must have
• Must be cool, edgy , contemporary and inviting

please see website www.silverorchardlane.com - as look and feel should tie in with that

photos and art work can be used from website and all our social media pages

```html
<!DOCTYPE html>
<html lang="en">
<head>
<meta charset="utf-8">
<title>Silver Orchard – Brochure Spread</title>
<link href="https://fonts.googleapis.com/css2?family=Parisienne&family=Mulish:wght@400;700&family=Tinos&display=swap" rel="stylesheet">
<style>
  :root {
    --ink: #1a1a1a;
    --black: #000;
    --white: #fff;
    --sky: #abdcea;
    --amber: #f6b042;
    --red: #e0282c;
    --grey-top: #a7aa9f;
    --grey-mid: #d6d7d1;
    --rule: #222;
  }
  * { margin: 0; padding: 0; box-sizing: border-box; }
  html, body { width: 1200px; height: 783px; overflow: hidden; background: var(--white); }
  .spread {
    position: relative; width: 1200px; height: 783px; overflow: hidden;
    font-family: "Mulish", sans-serif; color: var(--ink);
  }
  .page-right {
    position: absolute; left: 597px; top: 0; width: 603px; height: 783px;
    background: linear-gradient(180deg, var(--grey-top) 0%, var(--grey-mid) 28%, var(--white) 55%);
  }
  .photo-model-left {
    position: absolute; left: 0; top: 0; width: 292px; height: 783px;
    background: linear-gradient(180deg, #5a3a2c 0%, #3b2a24 30%, #111 45%, #161616 85%, #b3121a 100%);
  }
  .photo-model-right {
    position: absolute; left: 800px; top: 415px; width: 391px; height: 368px;
    background: linear-gradient(160deg, #eef0ef 0%, #d7dad9 55%, #a9adae 100%);
  }
  .heading-tab {
    position: absolute; background: var(--black); color: var(--white);
    font-family: "Parisienne", cursive; font-weight: 400; line-height: .85;
    padding: 10px 14px;
  }
  .tab-about { left: 403px; top: 124px; width: 194px; height: 48px; font-size: 34px; text-align: center; }
  .tab-benefits { left: 597px; top: 32px; width: 161px; height: 85px; font-size: 30px; }
  .tab-edge { left: 597px; top: 408px; width: 196px; height: 70px; font-size: 33px; }
  .panel-about {
    position: absolute; left: 305px; top: 172px; width: 292px; height: 234px;
    background: var(--sky); padding: 36px 10px 0 8px;
    font-size: 11.4px; letter-spacing: .15px; line-height: 1.62; text-align: justify;
  }
  .panel-edge {
    position: absolute; left: 597px; top: 478px; width: 196px; height: 270px;
    background: var(--amber); padding: 8px 8px 0 8px;
    font-size: 11.2px; line-height: 1.5; text-align: justify;
  }
  .panel-edge p + p { margin-top: 12px; }
  .title-block { position: absolute; left: 890px; top: 30px; color: var(--black); }
  .title-block .script { font-family: "Parisienne", cursive; font-size: 46px; line-height: 1; padding-left: 4px; }
  .title-block .caps { font-family: "Tinos", serif; font-size: 49px; color: var(--white); line-height: .9; }
  .benefits-rule { position: absolute; left: 667px; top: 137px; width: 2px; height: 212px; background: var(--rule); }
  .benefits { list-style: none; position: absolute; left: 667px; top: 152px; width: 500px; font-size: 13.2px; line-height: 1.35; }
  .benefits li { position: relative; padding-left: 28px; margin-bottom: 10px; }
  .benefits li::before { content: ""; position: absolute; left: 0; top: 8px; width: 22px; height: 2px; background: var(--rule); }
  .tagline { position: absolute; left: 233px; top: 480px; color: var(--red); line-height: 1.05; }
  .tagline > span { display: block; font-size: 19px; }
  .tagline .big { font-size: 37px; padding-left: 68px; }
  .tagline .l1 { padding-left: 2px; }
  .tagline .l3 { padding-left: 36px; }
  .tagline .l5 { padding-left: 30px; }
  .tagline .brand { font-size: 25px; }
  .brand-name {
    position: absolute; left: 305px; top: 684px; width: 285px; text-align: center;
    font-size: 28px; font-weight: 400; color: var(--ink); line-height: 1; white-space: nowrap;
  }
</style>
</head>
<body>
<main class="spread">
  <div class="page-right"></div>
  <div class="photo-model-left" role="img" aria-label="Photo of a model in a black peplum dress holding a red sequin clutch"></div>
  <div class="photo-model-right" role="img" aria-label="Photo of a model in grey jeans and a knit top crouching by a bright window"></div>

  <div class="title-block">
    <div class="script">fashion</div>
    <div class="caps">REDEFINED</div>
  </div>

  <h2 class="heading-tab tab-benefits">MemberShip<br>Benefits</h2>
  <div class="benefits-rule"></div>
  <ul class="benefits">
    <li>Sign up and get &nbsp;£25 &nbsp;credit</li>
    <li>Free UK express tracked and signed delivery on all orders</li>
    <li>Free international tracked and signed delivery on all orders over £100</li>
    <li>If you &nbsp;need to return an item, we will &nbsp;give you a £5 discount off your next purchase to make it up to you!</li>
    <li>We are very happy to provide a refund or exchange on all goods returned within 28 days of the date of dispatch for items that have not been worn, damaged or washed</li>
    <li>If you wish to exchange the item, please include in your email about details of what you would like instead and we will send you that item if it is in stock, otherwise we will offer you a refund</li>
  </ul>

  <h2 class="heading-tab tab-about">About Us</h2>
  <section class="panel-about">
    <p><strong>Silver Orchard</strong> is an online destination for edgy, indie, global design. It is a celebration of fashion – fashion which represents creativity, expression and rebellion. We look all over the world for exciting and emerging design talent to find something that brings something of the designer and his or her part of the world to your part of the world. We bring colour, fun and artistry, and something a little bit different and inspiring to life, through what we wear on our backs.</p>
  </section>

  <h2 class="heading-tab tab-edge">Our Unique<br>Edge</h2>
  <section class="panel-edge">
    <p>We don't slavishly follow seasons (after all it's always summer somewhere right?), we don't do here today gone tomorrow, fads and fast fashion, we don't do labels for the sake of labels, we don't do anything faux unless its faux fur. We value quality and good craftsmanship.</p>
    <p>We only sell what we love and what we know you will love. We revel in prints and pattern, unusual cuts, global influences, irreverence and comedy.</p>
  </section>

  <p class="tagline">
    <span class="l1">So take a day off from</span>
    <span class="big">the classic</span>
    <span class="l3">black trouser</span>
    <span>and indulge</span>
    <span class="l5">the <span class="brand">Silver Orchard</span> of you!</span>
  </p>

  <div class="brand-name">Silver Orchard</div>
</main>
</body>
</html>
```